Packaging Design for a Quenby sweets company.

We need a packaging design for a new company based in Kuwait named Quenby. We sell trifles in mini sizes and large sizes. (google what a trifle looks like)

I've already attached what the box looks like along with the layouts. All that is needed is drawing on the box.

It Company

• Must have Instagram and Whatsapp/phone number on the box.

Instagram account: quenby_z4
whatsapp/phone: 95318460

```html
<!DOCTYPE html>
<html lang="en">
<head>
<meta charset="utf-8">
<title>Quenby – Box Dieline</title>
<link rel="stylesheet" href="https://fonts.googleapis.com/css2?family=Tenor+Sans&display=swap">
<style>
  :root {
    --paper: #ffffff;
    --sky: #c9d6ee;
    --blush: #f8c8d3;
    --lilac: #dbbdd6;
    --mauve: #d7a0c0;
    --ink: #7c7c80;
    --frame: #b8b8bc;
    --cut: #b9b9bd;
  }
  html, body {
    margin: 0;
    padding: 0;
    width: 1200px;
    height: 927px;
    overflow: hidden;
    background: var(--paper);
  }
  .dieline {
    position: relative;
    width: 1200px;
    height: 927px;
    font-family: "Tenor Sans", sans-serif;
  }
  .dieline-art {
    position: absolute;
    inset: 0;
  }
  .brand-badge {
    position: absolute;
    left: 438px;
    top: 372px;
    width: 264px;
    height: 227px;
    box-sizing: border-box;
    background: var(--paper);
    border: 3px solid var(--frame);
    display: flex;
    flex-direction: column;
    align-items: center;
    justify-content: center;
    gap: 30px;
  }
  .brand-badge__mark {
    width: 104px;
    height: 84px;
    background: var(--blush);
  }
  .brand-badge__name {
    color: var(--ink);
    font-size: 40px;
    letter-spacing: 0.3em;
    margin-right: -0.3em;
    line-height: 1;
    white-space: nowrap;
  }
  .contact {
    position: absolute;
    color: var(--ink);
    line-height: 1.3;
    margin: 0;
    white-space: nowrap;
  }
  .contact--front {
    left: 712px;
    top: 673px;
    font-size: 16.5px;
  }
  .lid-flap {
    position: absolute;
    left: 179px;
    top: 8px;
    width: 790px;
    height: 170px;
    transform: rotate(180deg);
  }
  .lid-flap__name {
    position: absolute;
    right: 181px;
    bottom: 32px;
    color: var(--ink);
    font-size: 26px;
    letter-spacing: 0.3em;
    line-height: 1;
    white-space: nowrap;
  }
  .lid-flap__mark {
    position: absolute;
    right: 213px;
    bottom: 87px;
    width: 68px;
    height: 60px;
    background: var(--blush);
  }
  .contact--lid {
    left: 591px;
    top: 18px;
    font-size: 12.5px;
  }
</style>
</head>
<body>
<main class="dieline">
  <svg class="dieline-art" width="1200" height="927" viewBox="0 0 1200 927" xmlns="http://www.w3.org/2000/svg">
    <rect x="179" y="8" width="790" height="170" fill="var(--sky)"/>

    <g class="front-stripes">
      <rect x="179" y="178" width="790" height="567" fill="var(--blush)"/>
      <rect x="179" y="178" width="790" height="29" fill="var(--sky)"/>
      <rect x="179" y="207" width="790" height="7" fill="var(--mauve)"/>
      <rect x="179" y="214" width="790" height="24" fill="var(--paper)"/>
      <rect x="179" y="238" width="790" height="37" fill="var(--lilac)"/>
      <rect x="179" y="275" width="790" height="5" fill="var(--paper)"/>
      <rect x="179" y="295" width="790" height="6" fill="var(--mauve)"/>
      <rect x="179" y="318" width="790" height="6" fill="var(--sky)"/>
      <rect x="179" y="352" width="790" height="6" fill="var(--paper)"/>
      <rect x="179" y="358" width="790" height="20" fill="var(--sky)"/>
      <rect x="179" y="410" width="790" height="22" fill="var(--sky)"/>
      <rect x="179" y="432" width="790" height="40" fill="var(--lilac)"/>
      <rect x="179" y="472" width="790" height="6" fill="var(--paper)"/>
      <rect x="179" y="505" width="790" height="22" fill="var(--sky)"/>
      <rect x="179" y="527" width="790" height="41" fill="var(--lilac)"/>
      <rect x="179" y="568" width="790" height="7" fill="var(--paper)"/>
      <rect x="179" y="600" width="790" height="22" fill="var(--sky)"/>
      <rect x="179" y="622" width="790" height="40" fill="var(--lilac)"/>
      <rect x="179" y="662" width="790" height="6" fill="var(--paper)"/>
      <rect x="179" y="690" width="790" height="6" fill="var(--mauve)"/>
      <rect x="179" y="714" width="790" height="5" fill="var(--sky)"/>
    </g>

    <rect x="179" y="745" width="790" height="177" fill="var(--blush)"/>

    <rect x="8" y="178" width="171" height="567" fill="var(--blush)" role="img" aria-label="Pink side panel with white dotted pattern"/>
    <rect x="969" y="178" width="171" height="567" fill="var(--blush)" role="img" aria-label="Pink side panel with white dotted pattern"/>

    <g class="side-flap-stripes">
      <rect x="8" y="62" width="171" height="11" fill="var(--sky)"/>
      <rect x="8" y="75" width="171" height="5" fill="var(--mauve)"/>
      <rect x="8" y="80" width="171" height="15" fill="var(--sky)"/>
      <rect x="8" y="97" width="171" height="25" fill="var(--lilac)"/>
      <rect x="8" y="124" width="171" height="8" fill="var(--blush)"/>
      <rect x="8" y="132" width="171" height="6" fill="var(--mauve)"/>
      <rect x="8" y="138" width="171" height="12" fill="var(--blush)"/>
      <rect x="8" y="153" width="171" height="4" fill="var(--sky)"/>

      <rect x="969" y="62" width="171" height="11" fill="var(--sky)"/>
      <rect x="969" y="75" width="171" height="5" fill="var(--mauve)"/>
      <rect x="969" y="80" width="171" height="15" fill="var(--sky)"/>
      <rect x="969" y="97" width="171" height="25" fill="var(--lilac)"/>
      <rect x="969" y="124" width="171" height="8" fill="var(--blush)"/>
      <rect x="969" y="132" width="171" height="6" fill="var(--mauve)"/>
      <rect x="969" y="138" width="171" height="12" fill="var(--blush)"/>
      <rect x="969" y="153" width="171" height="4" fill="var(--sky)"/>
    </g>

    <g class="side-flap-stripes">
      <rect x="8" y="745" width="171" height="13" fill="var(--sky)"/>
      <rect x="8" y="760" width="171" height="5" fill="var(--mauve)"/>
      <rect x="8" y="765" width="171" height="13" fill="var(--sky)"/>
      <rect x="8" y="780" width="171" height="26" fill="var(--lilac)"/>
      <rect x="8" y="808" width="171" height="10" fill="var(--blush)"/>
      <rect x="8" y="818" width="171" height="6" fill="var(--mauve)"/>
      <rect x="8" y="824" width="171" height="10" fill="var(--blush)"/>
      <rect x="8" y="836" width="171" height="4" fill="var(--sky)"/>
      <rect x="8" y="840" width="171" height="18" fill="var(--blush)"/>

      <rect x="969" y="745" width="171" height="13" fill="var(--sky)"/>
      <rect x="969" y="760" width="171" height="5" fill="var(--mauve)"/>
      <rect x="969" y="765" width="171" height="13" fill="var(--sky)"/>
      <rect x="969" y="780" width="171" height="26" fill="var(--lilac)"/>
      <rect x="969" y="808" width="171" height="10" fill="var(--blush)"/>
      <rect x="969" y="818" width="171" height="6" fill="var(--mauve)"/>
      <rect x="969" y="824" width="171" height="10" fill="var(--blush)"/>
      <rect x="969" y="836" width="171" height="4" fill="var(--sky)"/>
      <rect x="969" y="840" width="171" height="18" fill="var(--blush)"/>
    </g>

    <g class="cut-lines" stroke="var(--cut)" stroke-width="1" fill="none">
      <line x1="48" y1="45" x2="140" y2="45"/>
      <line x1="1008" y1="45" x2="1100" y2="45"/>
      <line x1="48" y1="875" x2="140" y2="875"/>
      <line x1="1008" y1="875" x2="1100" y2="875"/>
      <line x1="179" y1="8" x2="969" y2="8"/>
      <line x1="179" y1="8" x2="179" y2="922"/>
      <line x1="969" y1="8" x2="969" y2="922"/>
      <line x1="8" y1="22" x2="8" y2="900"/>
      <line x1="1140" y1="22" x2="1140" y2="900"/>
      <line x1="179" y1="178" x2="969" y2="178"/>
      <line x1="179" y1="745" x2="969" y2="745"/>
    </g>
  </svg>

  <div class="lid-flap">
    <span class="lid-flap__name">quenby</span>
    <span class="lid-flap__mark"></span>
    <p class="contact contact--lid">Instagram Account: quenby_z4<br>whatsapp/phone: 95318460</p>
  </div>

  <div class="brand-badge">
    <span class="brand-badge__mark"></span>
    <span class="brand-badge__name">quenby</span>
  </div>

  <p class="contact contact--front">Instagram Account: quenby_z4<br>whatsapp/phone: 95318460</p>
</main>
</body>
</html>
```